Building Servicess

We need a new business card design for a company. We specialise in: Electrical/Site temporary electrics, Data/Network Installation, Passive Fire Protection

Industry/Entity Type

Construction

Contact Information for Business Card

Services provided as detailed on project description

Font styles to use
Serif

Colors
0054AA
0677BA
7BADD7
CADEEF
E8F1F8
00AB8E
00BBA5
67D7C9
C6EFE9
E9F9F6
EB3D1F
EC4F4E
F09395
F8D3D4
FCEDEE

Requirements
Must have
• Company logo-contact details-phone numbers

```html
<!DOCTYPE html>
<html lang="en">
<head>
<meta charset="utf-8">
<title>Brackwell Site Services – Business Card</title>
<link rel="stylesheet" href="https://fonts.googleapis.com/css2?family=Montserrat:wght@400;500;600;700&display=swap">
<style>
  :root {
    --page-bg: #c9c9c9;
    --brand-blue: #0f76c0;
    --brand-blue-deep: #0b68ae;
    --brand-blue-light: #2a88cc;
    --ink-grey: #3d3d3d;
    --rule-grey: #8a8a8a;
    --card-white: #ffffff;
    --soft-grey: #eef0f2;
  }
  html, body {
    margin: 0;
    padding: 0;
    width: 1200px;
    height: 900px;
    overflow: hidden;
    background: var(--page-bg);
    font-family: "Montserrat", Arial, sans-serif;
  }
  .canvas {
    position: relative;
    width: 1200px;
    height: 900px;
  }
  .card {
    position: absolute;
    left: 250px;
    width: 700px;
    height: 400px;
    border-radius: 34px;
    overflow: hidden;
    box-shadow: 0 10px 24px rgba(0,0,0,0.28);
  }
  .card-front {
    top: 30px;
    background: linear-gradient(100deg, var(--brand-blue-light) 0%, var(--brand-blue) 45%, var(--brand-blue-deep) 100%);
    color: var(--card-white);
  }
  .card-back {
    top: 470px;
    background: linear-gradient(110deg, var(--card-white) 0%, var(--card-white) 55%, var(--soft-grey) 100%);
    color: var(--ink-grey);
  }
  .light-band {
    position: absolute;
    top: 0;
    height: 100%;
    background: rgba(255,255,255,0.07);
  }
  .band-one { left: 60px; width: 150px; }
  .band-two { left: 260px; width: 120px; background: rgba(0,0,0,0.04); }
  .band-three { left: 470px; width: 110px; }

  .wordmark {
    display: flex;
    align-items: center;
    gap: 12px;
  }
  .wordmark-square {
    width: 20px;
    height: 20px;
    flex: none;
  }
  .wordmark-name {
    font-weight: 700;
    letter-spacing: 0.04em;
    white-space: nowrap;
  }
  .wordmark-rule {
    height: 2px;
    margin-top: 10px;
  }

  .front-brand {
    position: absolute;
    left: 120px;
    top: 120px;
    width: 460px;
  }
  .front-brand .wordmark-square { background: var(--card-white); }
  .front-brand .wordmark-name { font-size: 27px; color: var(--card-white); }
  .front-brand .wordmark-rule { background: var(--card-white); width: 100%; }

  .service-list {
    position: absolute;
    left: 0;
    right: 0;
    top: 250px;
    text-align: center;
    font-size: 15px;
    font-weight: 500;
    letter-spacing: 0.06em;
    line-height: 1.6;
    text-transform: uppercase;
  }

  .back-brand {
    position: absolute;
    left: 56px;
    top: 60px;
    width: 430px;
  }
  .back-brand .wordmark-square { background: var(--brand-blue); }
  .back-brand .wordmark-name { font-size: 25px; color: var(--brand-blue); }
  .back-brand .wordmark-rule { background: var(--rule-grey); width: 100%; }

  .holder {
    position: absolute;
    left: 56px;
    top: 185px;
  }
  .holder-name {
    font-size: 26px;
    font-weight: 700;
    color: var(--brand-blue);
    letter-spacing: 0.03em;
    text-transform: uppercase;
  }
  .holder-role {
    font-size: 15px;
    font-weight: 500;
    letter-spacing: 0.05em;
    text-transform: uppercase;
    margin-top: 2px;
  }
  .phone-list, .online-list {
    list-style: none;
    margin: 0;
    padding: 0;
  }
  .phone-list {
    position: absolute;
    left: 56px;
    top: 285px;
    font-size: 20px;
    font-weight: 500;
    line-height: 1.55;
  }
  .phone-list li, .online-list li {
    display: flex;
    align-items: center;
    gap: 12px;
  }
  .online-list {
    position: absolute;
    right: 44px;
    top: 130px;
    font-size: 17px;
    line-height: 1.7;
    text-align: right;
  }
  .online-list li { justify-content: flex-end; }
  .online-list .web-domain { color: var(--brand-blue); }
  .contact-icon {
    width: 20px;
    height: 20px;
    flex: none;
    stroke: var(--brand-blue);
    fill: none;
    stroke-width: 2;
  }
</style>
</head>
<body>
<main class="canvas">

  <section class="card card-front" aria-label="Card front">
    <div class="light-band band-one"></div>
    <div class="light-band band-two"></div>
    <div class="light-band band-three"></div>

    <div class="front-brand">
      <div class="wordmark">
        <span class="wordmark-square"></span>
        <span class="wordmark-name">BRACKWELL SITE SERVICES LTD</span>
      </div>
      <div class="wordmark-rule"></div>
    </div>

    <p class="service-list">
      Electrical/Site Temporary Electrics<br>
      Data/Network Installation | Passive Fire Protection
    </p>
  </section>

  <section class="card card-back" aria-label="Card back">
    <div class="back-brand">
      <div class="wordmark">
        <span class="wordmark-square"></span>
        <span class="wordmark-name">BRACKWELL SITE SERVICES LTD</span>
      </div>
      <div class="wordmark-rule"></div>
    </div>

    <div class="holder">
      <div class="holder-name">Daniel Hartley</div>
      <div class="holder-role">Managing Director</div>
    </div>

    <ul class="phone-list">
      <li>
        <svg class="contact-icon" viewBox="0 0 24 24" aria-hidden="true">
          <path d="M5 3h4l2 5-2.5 1.5a11 11 0 0 0 6 6L16 13l5 2v4a2 2 0 0 1-2 2A16 16 0 0 1 3 5a2 2 0 0 1 2-2z"/>
        </svg>
        <span>020 7946 0183</span>
      </li>
      <li>
        <svg class="contact-icon" viewBox="0 0 24 24" aria-hidden="true">
          <rect x="6" y="2" width="12" height="20" rx="2"/>
          <line x1="11" y1="18" x2="13" y2="18"/>
        </svg>
        <span>07700900412</span>
      </li>
    </ul>

    <ul class="online-list">
      <li>
        <span>info@brackwellsite.com</span>
        <svg class="contact-icon" viewBox="0 0 24 24" aria-hidden="true">
          <rect x="2" y="5" width="20" height="14" rx="1"/>
          <polyline points="2,6 12,13 22,6"/>
        </svg>
      </li>
      <li>
        <span>www.<span class="web-domain">brackwellsite</span>.com</span>
        <svg class="contact-icon" viewBox="0 0 24 24" aria-hidden="true">
          <circle cx="12" cy="12" r="9"/>
          <ellipse cx="12" cy="12" rx="4" ry="9"/>
          <line x1="3" y1="12" x2="21" y2="12"/>
        </svg>
      </li>
    </ul>
  </section>

</main>
</body>
</html>
```